Webbanner-Design holvira.at Webshop
Zielgruppe
Onlineshop für Haus + Garten
holvira.at
Aufgabenstellung
Benötigt wird ein neues Banner-Set
ein Allgemeines - warum bei holvira.at einkaufen
- günstige Preise durch Direktbezug ohne Zwischenhandel
- alle Artikel vorrätig - schnelle Lieferung
- Sichere Kaufabwicklung - Lumena Kauf
- Fachberatung und Service durch geschultes Peronal
sowie Banner für jede Hauptkategorie

```html
<!DOCTYPE html>
<html lang="de">
<head>
<meta charset="utf-8">
<title>holvira.at – Webshop</title>
<link href="https://fonts.googleapis.com/css2?family=Open+Sans:wght@400;600;700;800&display=swap" rel="stylesheet">
<style>
:root{
  --navy:#1f3f86;
  --navy-light:#2b68ad;
  --gold:#c9a95c;
  --link:#3f8fd6;
  --nav-text:#555;
  --white:#fff;
  --dark-btn:#333;
  --border:#ccc;
}
*{box-sizing:border-box;margin:0;padding:0}
html,body{width:1200px;height:745px;overflow:hidden}
body{font-family:'Open Sans',sans-serif;background:var(--white);position:relative}
.topbar-links{position:absolute;top:14px;left:886px;font-size:12px;display:flex}
.topbar-links a{color:var(--link);text-decoration:none;padding:0 6px;border-left:1px solid #ccc}
.topbar-links a:first-child{border-left:none}
.lang-btn{position:absolute;left:1069px;top:13px;width:76px;height:21px;background:var(--dark-btn);color:#fff;font-size:11px;border-radius:3px;display:flex;align-items:center;justify-content:center;gap:3px}
.brand{position:absolute;left:55px;top:40px;display:flex;align-items:center;gap:8px}
.brand-square{width:20px;height:20px;background:var(--navy)}
.brand-name{font-size:26px;font-weight:700;color:var(--gold);letter-spacing:-0.5px}
.badge{position:absolute;left:342px;top:36px;width:52px;height:52px;border-radius:50%;background:var(--navy);border:3px solid #e8e8e8}
.search{position:absolute;left:676px;top:49px;width:242px;height:36px;border:1px solid var(--border);border-radius:3px;display:flex}
.search-input{flex:1;font-size:13px;color:#999;padding:8px 12px}
.search-btn{width:40px;border-left:1px solid var(--border);background:#f3f3f3;display:flex;align-items:center;justify-content:center}
.account{position:absolute;left:947px;top:65px;color:var(--link);font-size:14px;display:flex;align-items:center;gap:4px}
.cart{position:absolute;left:1068px;top:65px;color:var(--link);font-size:14px;display:flex;align-items:center;gap:4px}
.caret{display:inline-block;border-left:4px solid transparent;border-right:4px solid transparent;border-top:4px solid currentColor;vertical-align:middle;margin-left:4px}
.main-nav{position:absolute;top:111px;left:0;width:1200px;height:60px;background:linear-gradient(#fff,#ececec);display:flex;align-items:center;padding-left:64px}
.main-nav span{font-size:13.5px;color:var(--nav-text);margin-right:29px}
.stage{position:absolute;top:171px;left:0;width:1200px;height:574px;background:linear-gradient(90deg,#7d93a3 0%,#b8c8cf 6%,#4f8fae 50%,#a9c6cf 95%,#6e98a7 100%)}
.panel{position:absolute;left:50px;top:185px;width:1101px;height:550px;background:var(--white)}
.banner{position:absolute;left:73px;top:207px;width:1055px;height:440px}
.banner-bg{position:absolute;left:0;top:0}
.banner-copy{position:absolute;left:38px;top:34px;color:var(--white)}
.kicker{font-size:16.5px;font-weight:400}
.kicker b{font-weight:700}
.headline{margin-top:22px;font-size:36px;font-weight:800;line-height:41px}
.usp{margin-top:26px;list-style:none}
.usp li{font-size:21.5px;font-weight:700;line-height:28px;display:flex;align-items:center;gap:7px}
.chevron{flex:none;width:14px;height:18px}
.cta{position:absolute;left:891px;top:276px;width:126px;height:126px;border-radius:50%;background:var(--gold);color:#fff;font-weight:700;font-size:14px;line-height:19px;display:flex;align-items:center;justify-content:center;text-align:center}
.dots{position:absolute;top:686px;left:520px;display:flex;gap:19px;align-items:center}
.dots i{width:6px;height:6px;border-radius:50%;background:#333;display:block}
.dots i.active{width:11px;height:11px;background:#fff;border:2px solid #333}
</style>
</head>
<body>
<nav class="topbar-links"><a>News</a><a>Kontakt</a><a>Links</a></nav>
<div class="lang-btn">Deutsch<span class="caret"></span></div>

<div class="brand"><span class="brand-square"></span><span class="brand-name">holvira.at</span></div>
<div class="badge" role="img" aria-label="Gütesiegel"></div>

<div class="search">
  <div class="search-input">Suchen</div>
  <div class="search-btn"><svg width="16" height="16" viewBox="0 0 16 16"><circle cx="6.5" cy="6.5" r="5" fill="none" stroke="#3f8fd6" stroke-width="2"/><line x1="10" y1="10" x2="15" y2="15" stroke="#3f8fd6" stroke-width="2.4"/></svg></div>
</div>
<div class="account"><svg width="11" height="12" viewBox="0 0 11 12"><circle cx="5.5" cy="3" r="3" fill="#3f8fd6"/><path d="M0 12 C0 7 11 7 11 12 Z" fill="#3f8fd6"/></svg>Anmelden<span class="caret"></span></div>
<div class="cart"><svg width="13" height="12" viewBox="0 0 13 12"><path d="M0 1 H2.5 L4 8 H11 L12.5 3 H3" fill="none" stroke="#3f8fd6" stroke-width="1.6"/><circle cx="5" cy="10.5" r="1.3" fill="#3f8fd6"/><circle cx="10" cy="10.5" r="1.3" fill="#3f8fd6"/></svg>0,00 €<span class="caret"></span></div>

<nav class="main-nav">
  <span>Badezimmer<i class="caret"></i></span>
  <span>Schwimmbecken<i class="caret"></i></span>
  <span>Schwimmbadzubehör<i class="caret"></i></span>
  <span>Sauna</span>
  <span>Heizung, Solar, Klima<i class="caret"></i></span>
  <span>Garten<i class="caret"></i></span>
  <span>Kabelkanal</span>
  <span>Whirlpoolzubehör<i class="caret"></i></span>
</nav>

<div class="stage" role="img" aria-label="Unscharfer Poolhintergrund"></div>
<div class="panel"></div>

<section class="banner">
  <svg class="banner-bg" viewBox="0 0 1055 440" width="1055" height="440">
    <defs>
      <linearGradient id="blueFill" x1="0" y1="0" x2="1" y2="1">
        <stop offset="0" stop-color="#1f3b80"/>
        <stop offset="1" stop-color="#2b6aae"/>
      </linearGradient>
      <linearGradient id="photoFill" x1="0" y1="0" x2="0" y2="1">
        <stop offset="0" stop-color="#3fb2d8"/>
        <stop offset="0.45" stop-color="#c99a78"/>
        <stop offset="1" stop-color="#b89a7a"/>
      </linearGradient>
    </defs>
    <rect x="0" y="0" width="1055" height="440" fill="url(#photoFill)" role="img" aria-label="Foto: lächelnde Familie am Beckenrand im Pool"/>
    <path d="M0 0 H494 C410 120 380 300 479 440 H0 Z" fill="#c9a95c"/>
    <path d="M0 0 H448 C380 120 370 300 465 440 H0 Z" fill="url(#blueFill)"/>
  </svg>
  <div class="banner-copy">
    <p class="kicker"><b>IHR FACHMANN</b> FÜR BAD, POOL UND MEHR</p>
    <h1 class="headline">WILLKOMMEN<br>BEIM PROFI</h1>
    <ul class="usp">
      <li><svg class="chevron" viewBox="0 0 14 18"><path d="M0 1 H6 L14 9 L6 17 H0 L8 9 Z" fill="#c9a95c"/></svg>GÜNSTIGE PREISE</li>
      <li><svg class="chevron" viewBox="0 0 14 18"><path d="M0 1 H6 L14 9 L6 17 H0 L8 9 Z" fill="#c9a95c"/></svg>KOMPETENTER SERVICE</li>
      <li><svg class="chevron" viewBox="0 0 14 18"><path d="M0 1 H6 L14 9 L6 17 H0 L8 9 Z" fill="#c9a95c"/></svg>SCHNELLE LIEFERUNG</li>
      <li><svg class="chevron" viewBox="0 0 14 18"><path d="M0 1 H6 L14 9 L6 17 H0 L8 9 Z" fill="#c9a95c"/></svg>SICHERES SHOPPING</li>
    </ul>
  </div>
  <div class="cta">MEHR<br>ERFAHREN</div>
</section>

<div class="dots"><i></i><i></i><i></i><i></i><i class="active"></i><i></i><i></i></div>
</body>
</html>
```